Come as U R - mental health service LGBTIQ inclusive poster

We are a mental health organisation in Australia that is looking for a poster design that we can put in our waiting rooms to show that our service is inclusive of gender diverse, intersex, and sexuality diverse people. We will add text and our company logo afterwards. An example has been provided for inspiration. Designers 25 and under encouraged.

Target Market(s)

Target audience - all genders 12-25.

Industry/Entity Type

Mental Health

Requirements
Must have
• This graphic should be colourful, include the text "Come as U R", and incorporate the colours of the pride flag. Should be a general design that is appropriate for all of the target audience.

```html
<!DOCTYPE html>
<html lang="en">
<head>
<meta charset="utf-8">
<title>Come as U R</title>
<link rel="stylesheet" href="https://fonts.googleapis.com/css2?family=Fredoka:wght@600&display=swap">
<style>
  :root {
    --pride-red: #e8251c;
    --pride-red-deep: #b8140f;
    --pride-orange: #f08a1c;
    --pride-orange-deep: #c9650e;
    --pride-yellow: #f2e33a;
    --pride-yellow-deep: #c9b81c;
    --pride-green: #3fb23a;
    --pride-green-deep: #24802a;
    --pride-blue: #8fa8e0;
    --pride-blue-deep: #5f79bd;
    --crowd-grey: #d9cfd3;
    --crowd-grey-deep: #9e9498;
    --ink-blue: #1446b8;
    --rule-purple: #7a1aa0;
    --rule-yellow: #fff200;
    --rule-green: #49e21a;
    --letter-white: #ffffff;
    --letter-red: #ee1c1c;
    --letter-yellow: #ffe812;
    --heart-green: #3de23a;
    --heart-yellow: #f4ec2c;
    --heart-white: #f4f4f4;
    --heart-orange: #f07a1e;
  }
  html, body {
    margin: 0;
    padding: 0;
    width: 849px;
    height: 1200px;
    overflow: hidden;
    background: #ffffff;
  }
  .poster {
    display: block;
    width: 849px;
    height: 1200px;
  }
  .headline {
    font-family: "Fredoka", "Arial Rounded MT Bold", sans-serif;
    font-weight: 600;
    paint-order: stroke fill;
    stroke-linejoin: round;
  }
  .headline-come { fill: var(--letter-white); stroke: var(--ink-blue); stroke-width: 16px; }
  .headline-as { fill: var(--letter-yellow); stroke: var(--letter-red); stroke-width: 16px; }
  .headline-u { fill: var(--letter-red); stroke: var(--letter-yellow); stroke-width: 16px; }
  .headline-r { fill: var(--letter-red); stroke: var(--letter-white); stroke-width: 16px; }
  .wavy-rule { fill: none; stroke-width: 12px; stroke-linecap: round; }
  .rule-blue { stroke: var(--ink-blue); }
  .rule-purple { stroke: var(--rule-purple); }
  .rule-yellow { stroke: var(--rule-yellow); }
  .rule-green { stroke: var(--rule-green); }
  .torn-strip { fill: #ffffff; }
</style>
</head>
<body>
<svg class="poster" viewBox="0 0 849 1200" xmlns="http://www.w3.org/2000/svg">
  <defs>
    <linearGradient id="tint-red" x1="0" y1="0" x2="1" y2="1">
      <stop offset="0" stop-color="var(--pride-red-deep)"/><stop offset="1" stop-color="var(--pride-red)"/>
    </linearGradient>
    <linearGradient id="tint-orange" x1="0" y1="0" x2="1" y2="1">
      <stop offset="0" stop-color="var(--pride-orange-deep)"/><stop offset="1" stop-color="var(--pride-orange)"/>
    </linearGradient>
    <linearGradient id="tint-yellow" x1="0" y1="0" x2="1" y2="1">
      <stop offset="0" stop-color="var(--pride-yellow-deep)"/><stop offset="1" stop-color="var(--pride-yellow)"/>
    </linearGradient>
    <linearGradient id="tint-green" x1="0" y1="0" x2="1" y2="1">
      <stop offset="0" stop-color="var(--pride-green-deep)"/><stop offset="1" stop-color="var(--pride-green)"/>
    </linearGradient>
    <linearGradient id="tint-blue" x1="0" y1="0" x2="1" y2="1">
      <stop offset="0" stop-color="var(--pride-blue-deep)"/><stop offset="1" stop-color="var(--pride-blue)"/>
    </linearGradient>
    <linearGradient id="tint-grey" x1="0" y1="0" x2="1" y2="1">
      <stop offset="0" stop-color="var(--crowd-grey-deep)"/><stop offset="1" stop-color="var(--crowd-grey)"/>
    </linearGradient>
  </defs>

  <g class="crowd-bands">
    <rect class="crowd-band" role="img" aria-label="Crowd of smiling people waving, tinted red" x="0" y="0" width="849" height="200" fill="url(#tint-red)"/>
    <rect class="crowd-band" role="img" aria-label="Crowd of smiling people waving, tinted orange" x="0" y="200" width="849" height="198" fill="url(#tint-orange)"/>
    <rect class="crowd-band" role="img" aria-label="Crowd of smiling people waving, tinted yellow" x="0" y="398" width="849" height="200" fill="url(#tint-yellow)"/>
    <rect class="crowd-band" role="img" aria-label="Crowd of smiling people cheering, tinted green" x="0" y="598" width="849" height="214" fill="url(#tint-green)"/>
    <rect class="crowd-band" role="img" aria-label="Crowd of people clapping, tinted blue" x="0" y="812" width="849" height="186" fill="url(#tint-blue)"/>
    <rect class="crowd-band" role="img" aria-label="Crowd of laughing people in black and white" x="0" y="998" width="849" height="202" fill="url(#tint-grey)"/>
  </g>

  <path class="torn-strip" d="M0 168 L90 172 L160 166 L260 174 L380 168 L470 175 L560 167 L680 174 L760 168 L849 172 L849 200 L760 196 L640 202 L520 195 L400 201 L300 194 L180 200 L80 195 L0 199 Z"/>

  <path class="wavy-rule rule-blue" d="M0 397 Q120 390 240 396 T480 395 T720 393 T849 396"/>
  <path class="wavy-rule rule-purple" d="M0 598 Q140 590 280 597 T560 596 T849 594"/>
  <path class="wavy-rule rule-yellow" d="M0 812 Q140 804 280 811 T560 816 T849 810"/>
  <path class="wavy-rule rule-green" d="M0 998 Q140 990 280 996 T560 1000 T849 995"/>

  <text class="headline headline-come" x="10" y="368" font-size="320" textLength="830" lengthAdjust="spacingAndGlyphs">come</text>
  <text class="headline headline-as" x="295" y="560" font-size="270" textLength="265" lengthAdjust="spacingAndGlyphs">as</text>
  <text class="headline headline-u" x="85" y="985" font-size="585" textLength="285" lengthAdjust="spacingAndGlyphs">U</text>
  <text class="headline headline-r" x="455" y="985" font-size="585" textLength="390" lengthAdjust="spacingAndGlyphs">R.</text>

  <g class="scribble-hearts">
    <rect role="img" aria-label="Green scribbled heart" x="720" y="22" width="100" height="95" rx="40" fill="var(--heart-green)" transform="rotate(-10 770 70)"/>
    <rect role="img" aria-label="Yellow scribbled heart" x="548" y="665" width="110" height="110" rx="44" fill="var(--heart-yellow)"/>
    <rect role="img" aria-label="White scribbled heart" x="172" y="795" width="115" height="110" rx="44" fill="var(--heart-white)"/>
    <rect role="img" aria-label="Orange scribbled heart" x="20" y="1030" width="125" height="120" rx="48" fill="var(--heart-orange)"/>
  </g>
</svg>
</body>
</html>
```